Casa Orvella Postcard

Please refer to our site for inspiration - I know this is alot of info but ?

Casa Orvella Reception Hall
4182C Tamsen Ave, Benicia, CA 707-555-0148
www.Casa-Orvella.example

Located in Benicia, California, we are a new venue that can host a variety of events. We can provide an exceptional space for your next party, reception, quinceañera, birthday party, or meeting! We treat each client with respect and go out of our way to accommodate all of your needs and make your event a success. Conveniently located just off the 680/780 junction, Casa Orvella is located in a safe, well-lit area with a large private parking area.

The space comes prepared with everything you need to get your party started – chairs and tables with tablecloths, a well-equipped kitchen, and incredible decorations to set the perfect backdrop to your event! Rent just the Lounge for a more intimate get-together, or add the Main Hall for your large sit-down event.

Lounge – Beautiful 1,600 ft2 entry room featuring large living room with conversation sofa seating for 40+ Sound system  Pass-through bar with seating  Fully-equipped 200 ft2 kitchen with
4-burner gas stove, oven, large double sink, full-size refrigerator, 2 microwaves, and ice machine, plus lots of storage and counter space  Newly-remodeled Men’s and Women’s bathrooms

Main Hall – Spacious 24’x80’ room with seating for up to 160 people  2,000 ft2  72” round tables with chairs, each seating up to 8 guests  DJ stand and Sound system  Atmospheric lighting
_______________________________________
Pricing -
Daytime Parties
Available 8AM-2PM
4-hour minimum

Lounge and Kitchen Only
Fri - Sat - Sun : $80/hr
Mon - Thurs : $60/hr

All Areas: Lounge, Kitchen, Main Hall, and Backyard
Fri - Sat - Sun : $120/hr
Mon - Thurs : $100/hr
___________________________________________
Evening Events
Available 3PM-12AM
5-hour minimum

Lounge and Kitchen Only -
Fri - Sat - Sun : $100/hr
Mon - Thurs : $50/hr

Fri - Sat - Sun : $160/hr
Mon - Thurs : $75/hr
___________________________________________________
Looking for a different time frame, all-day rental, or other special request? Let us know!
We'd be happy to provide you with a custom quote for your event.
Updates

I am not going to mail this postcard - only a hand out I need info and pricing on back

Target Market(s)

This is a hand out - will not be mailed

Only need my text on back

Industry/Entity Type

Parking

Requirements
Must have
• Text and pricing on back
Should not have
• Vintage feel to it

```html
<!DOCTYPE html>
<html lang="en">
<head>
<meta charset="utf-8">
<title>Casa Orvella Postcard</title>
<link rel="stylesheet" href="https://fonts.googleapis.com/css2?family=Allura&family=Roboto+Condensed:wght@700&family=Pathway+Gothic+One&display=swap">
<style>
  :root {
    --page: #ffffff;
    --slate: #6d7aa4;
    --ink: #262626;
    --script-gold: #e2b487;
    --banner-red: #a3282a;
    --tan: #c08f66;
    --tan-ink: #3a3330;
    --white: #ffffff;
    --note-box: #444444;
    --note-text: #d8d8d8;
    --photo-warm-a: #5a4536;
    --photo-warm-b: #c9b59a;
  }
  * { margin: 0; padding: 0; box-sizing: border-box; }
  html, body { width: 1200px; height: 1000px; overflow: hidden; background: var(--page); }
  .canvas { position: relative; width: 1200px; height: 1000px; }

  /* Front card */
  .front { position: absolute; left: 59px; top: 52px; width: 689px; height: 533px; background: var(--slate); overflow: hidden; }
  .photo { position: absolute; }
  .photo-lounge { left: 0; top: 0; width: 476px; height: 300px; overflow: hidden;
    background: linear-gradient(160deg, #8c7a63 0%, var(--photo-warm-b) 35%, #6b5442 65%, var(--photo-warm-a) 100%); }
  .photo-hall { left: 183px; top: 351px; width: 163px; height: 182px;
    background: linear-gradient(180deg, #3a2f28 0%, #7d6a58 45%, #cbbba6 70%, #4a3a2e 100%); }
  .photo-buffet { left: 353px; top: 351px; width: 336px; height: 182px;
    background: linear-gradient(175deg, #5e4c3e 0%, #d7c8b0 40%, #8a7560 70%, #efe6d8 100%); }

  .banner { position: absolute; left: -48px; top: 92px; width: 340px; height: 26px; background: var(--banner-red);
    transform: rotate(-17deg); transform-origin: left top; padding-left: 58px; white-space: nowrap;
    font: 700 12.5px/26px "Roboto Condensed", sans-serif; color: var(--white); text-align: left; }

  .venue-name { position: absolute; left: 28px; top: 254px; font: 400 84px/1 "Allura", cursive; color: var(--white); white-space: nowrap; }

  .script-head { font: 400 24px/1 "Allura", cursive; color: var(--script-gold); }
  .details { font: 700 13px/17.4px "Roboto Condensed", sans-serif; color: var(--ink); letter-spacing: -0.2px; }

  .lounge { position: absolute; left: 491px; top: 14px; width: 168px; }
  .lounge .script-head { margin-bottom: 8px; }
  .main-hall { position: absolute; left: 16px; top: 362px; width: 168px; }
  .main-hall .script-head { margin-bottom: 8px; }

  /* Back card */
  .back { position: absolute; left: 646px; top: 548px; width: 510px; height: 396px; background: var(--tan); font-family: "Pathway Gothic One", sans-serif; }
  .back-title { position: absolute; left: 0; width: 510px; top: 10px; text-align: center; font: 400 38px/1 "Allura", cursive; color: var(--white); }
  .dotted-rule { position: absolute; left: 37px; top: 59px; width: 436px; border-top: 3px dotted #4d4540; }
  .pricing-label { position: absolute; left: 0; width: 510px; top: 74px; text-align: center; font-size: 21px; line-height: 24px; color: var(--tan-ink); }
  .divider { position: absolute; left: 254px; top: 100px; width: 1.5px; height: 168px; background: #5a4e46; }
  .column { position: absolute; top: 94px; width: 230px; text-align: center; font-size: 14.5px; line-height: 15.4px; color: var(--tan-ink); }
  .column.day { left: 9px; }
  .column.evening { left: 271px; }
  .column h3 { font-weight: 400; font-size: 14.5px; color: var(--white); margin-bottom: 9px; }
  .column .hours { margin-bottom: 14px; }
  .column .rate-group { margin-bottom: 15px; }
  .price { color: var(--white); }
  .note { position: absolute; left: 40px; top: 294px; width: 428px; height: 88px; background: var(--note-box);
    color: var(--note-text); text-align: center; font-size: 14.5px; line-height: 20.5px; padding-top: 12px; }
</style>
</head>
<body>
<div class="canvas">

  <section class="front">
    <div class="photo photo-lounge" role="img" aria-label="Photo of the lounge with brown sofas, lamps and tall windows"></div>
    <div class="photo photo-hall" role="img" aria-label="Photo of the main hall with round tables and string lights"></div>
    <div class="photo photo-buffet" role="img" aria-label="Photo of a buffet table set up in the lounge"></div>

    <div class="banner">The ultimate event venue! Book today!</div>

    <div class="venue-name">Casa Orvella</div>

    <div class="lounge">
      <div class="script-head">Lounge</div>
      <p class="details">Beautiful 1,600 ft, 2 entry room featuring large living room with conversation sofa seating for 40+<br>
      • Sound system<br>
      • Pass-through bar with seating<br>
      • Fully-equipped 200ft kitchen with 4-burner gas stove, oven, large double sink, full-size refrigerator, 2 microwaves, and ice machine, plus lots of storage and counter space<br>
      • Newly-remodeled Men’s and Women’s bathrooms</p>
    </div>

    <div class="main-hall">
      <div class="script-head">Main Hall</div>
      <p class="details">Spacious 24’x 80’ room with seating for up to 160 people<br>
      • 72” round tables with chairs, each seating up to 8 guests<br>
      • DJ stand and Sound system<br>
      • Atmospheric lighting</p>
    </div>
  </section>

  <section class="back">
    <div class="back-title">Casa Orvella</div>
    <div class="dotted-rule"></div>
    <div class="pricing-label">— PRICING —</div>
    <div class="divider"></div>

    <div class="column day">
      <h3>Daytime Parties</h3>
      <p class="hours">Available 8am-2pm | 4-hour minimum</p>
      <p class="rate-group">Lounge and Kitchen Only<br>Fri - Sat - Sun : <span class="price">$80/hr</span><br>Mon - Thurs : <span class="price">$60/hr</span></p>
      <p class="rate-group">All Areas: Lounge, Kitchen, Main<br>Hall, and Backyard<br>Fri - Sat - Sun : <span class="price">$120/hr</span><br>Mon - Thurs : <span class="price">$100/hr</span></p>
    </div>

    <div class="column evening">
      <h3>Evening Parties</h3>
      <p class="hours">Available 3pm-Midnight | 5-hour minimum</p>
      <p class="rate-group">Lounge and Kitchen Only -<br>Fri - Sat - Sun : <span class="price">$100/hr</span><br>Mon - Thurs : <span class="price">$50/hr</span></p>
      <p class="rate-group">All Areas: Lounge, Kitchen, Main<br>Hall, and Backyard<br>Fri - Sat - Sun : <span class="price">$160/hr</span><br>Mon - Thurs : <span class="price">$75/hr</span></p>
    </div>

    <div class="note">Looking for a different time frame, all-day rental,<br>or other special request? Let us know!<br>We’d be happy to provide you with a custom quote for your event.</div>
  </section>

</div>
</body>
</html>
```